VornaDerm/The experts in permanent hairremoval

Our Brand is VornaDerm and we are specialized on permantent hair removal for the body for men and woman. VornaDerm is working as a Franchise chain.
The brand should be positioned as lifestyle brand but with a medical background. People should trust in us. We take care about their body. This need to be communicated 100%.
Our system is inexpensive but we don't want to show that we are cheap. So we want to communicate that permanent hair removal is a real lifestyle product but affordable.
We already created a logo that you can see the style and colour we prefer.

Target Market(s)

Europe beginning (especially german spoken markets), Middle East, Africa

Industry/Entity Type

Hair Removal

Number of Pages Required

5+ page

Font styles to use
Serif
Other font styles liked:
• Trajan Pro

Requirements
Nice to have
• We are very open for new ideas

```html
<!DOCTYPE html>
<html lang="en">
<head>
<meta charset="utf-8">
<title>VornaDerm – Permanent Hair Removal</title>
<link rel="stylesheet" href="https://fonts.googleapis.com/css2?family=Cinzel:wght@400;500;600&family=Open+Sans:wght@400;600&display=swap">
<style>
:root{
  --blue:#1a6fb5;
  --sky:#4aa9de;
  --hero-sky:#5db2e3;
  --cta:#00aeef;
  --ink:#222;
  --nav:#444;
  --muted:#7a7a80;
  --red:#c8283c;
  --band:#7b7c82;
  --placeholder-a:#d9c7bd;
  --placeholder-b:#c4aa9b;
  --panel:#e7e1e3;
  --field:#f1eef0;
  --field-line:#6b2d55;
  --navy:#1d2a80;
  --footer:#5b5b69;
}
*{margin:0;padding:0;box-sizing:border-box}
html,body{width:1200px;height:788px;overflow:hidden;background:#fff}
body{position:relative;font-family:"Open Sans",Arial,sans-serif;color:var(--ink)}
.abs{position:absolute}

.site-header{position:absolute;left:0;top:0;width:1200px;height:120px;border-bottom:2px solid var(--red);background:#fff}
.brand-mark{left:127px;top:28px;width:34px;height:34px;border-radius:50%;background:var(--sky)}
.brand-name{left:198px;top:20px;font-size:40px;font-weight:400;color:var(--muted);line-height:1.2}
.tagline{left:206px;top:75px;font-family:"Cinzel",serif;font-size:8.5px;letter-spacing:.3px;color:var(--muted)}
.util-links{right:205px;top:22px;font-size:13px;color:var(--sky)}
.util-links span{margin:0 6px}
.main-nav{right:205px;top:56px;display:flex;gap:20px;font-size:13px;color:var(--nav)}

.hero-band{left:0;top:120px;width:1200px;height:333px;background:var(--band)}
.hero-photo{left:78px;top:120px;width:1043px;height:333px;
  background:linear-gradient(180deg,var(--placeholder-a) 0%,var(--placeholder-b) 100%)}
.hero-caption{left:78px;top:279px;width:615px;height:136px;background:rgba(48,30,22,.78)}
.hero-title{left:100px;top:314px;font-family:"Cinzel",serif;font-size:39px;letter-spacing:1px;color:var(--hero-sky);line-height:1}
.hero-sub{left:100px;top:357px;font-size:24px;color:#fff;line-height:1.1}

.intro{left:171px;top:492px;width:500px}
.intro h2{font-family:"Cinzel",serif;font-weight:600;font-size:22px;letter-spacing:.4px;color:var(--blue);margin-left:-1px}
.intro p{margin-top:12px;font-family:Arial,Helvetica,sans-serif;font-size:12px;line-height:22px;color:var(--ink);padding-left:2px}
.intro .more{display:block;margin-top:10px;padding-left:1px;font-family:Arial,Helvetica,sans-serif;font-size:12px;font-weight:bold;color:var(--navy);text-decoration:none}

.login-panel{left:717px;top:421px;width:260px;height:263px;background:var(--panel);border:1px solid #2f7fc1}
.login-panel h3{position:absolute;left:15px;top:18px;font-weight:400;font-size:17px;color:var(--blue)}
.login-panel label{position:absolute;left:21px;font-family:Arial,Helvetica,sans-serif;font-size:12px;color:#222}
.login-panel .field{position:absolute;left:21px;width:185px;height:30px;background:var(--field);border:1px solid var(--field-line)}
.btn-login{position:absolute;left:21px;top:195px;width:96px;height:32px;background:var(--cta);border:2px solid #fff;color:#fff;font-weight:600;font-size:14px;display:flex;align-items:center;justify-content:center}
.register{position:absolute;left:127px;top:206px;font-family:Arial,Helvetica,sans-serif;font-size:11px;font-weight:bold;color:var(--blue)}

.site-footer{left:0;top:756px;width:1200px;height:32px;background:var(--footer);color:#eee;font-family:Arial,Helvetica,sans-serif;font-size:10.5px;display:flex;align-items:center;justify-content:center;letter-spacing:.3px}
</style>
</head>
<body>
<header class="site-header">
  <span class="abs brand-mark"></span>
  <span class="abs brand-name">VornaDerm</span>
  <div class="abs tagline">The experts in permanent hair removal</div>
  <div class="abs util-links">Jobs<span>|</span>Franchise</div>
  <nav class="abs main-nav"><span>Home</span><span>Why Permanent Epilation</span><span>Book Appointment</span><span>About</span><span>Contact</span></nav>
</header>

<div class="abs hero-band"></div>
<div class="abs hero-photo" role="img" aria-label="Photo of a practitioner performing laser hair removal treatment on a client"></div>
<div class="abs hero-caption"></div>
<div class="abs hero-title">PERMANENT HAIR REMOVAL</div>
<div class="abs hero-sub">FOR MEN AND WOMEN</div>

<section class="abs intro">
  <h2>AFFORDABLE &amp; 100% SAFE</h2>
  <p>Lorem ipsum dolor sit amet, consectetur adipisicing elit, sed do eiusmod tempor incididunt ut labore et dolore magna aliqua. Ut enim ad minim veniam, quis nostrud exercitation ullamco laboris nisi ut aliquip ex ea commodo consequat. Duis aute irure dolor in reprehenderit in voluptate velit esse cillum dolore eu fugiat nulla pariatur. Excepteur sint occaecat cupidatat non proident, sunt in culpa qui officia deserunt mollit anim id est laborum.</p>
  <a class="more" href="#">Learn more....</a>
</section>

<aside class="abs login-panel">
  <h3>Franchise Login</h3>
  <label style="top:56px">Username</label>
  <div class="field" style="top:83px"></div>
  <label style="top:131px">Password</label>
  <div class="field" style="top:152px"></div>
  <div class="btn-login">Login</div>
  <span class="register">Register</span>
</aside>

<footer class="abs site-footer">© 2015&nbsp; VornaDerm</footer>
</body>
</html>
```